Business Card

Just need business logo with phone number on it. 0472 318 506
And the following on the bottom of the card.

"Your local plumbing experts".
and emblems for kovo card, cheque and cash

```html
<!DOCTYPE html>
<html lang="en">
<head>
<meta charset="utf-8">
<title>Ridgeway Plumbing &amp; Drainage – Business Card</title>
<link href="https://fonts.googleapis.com/css2?family=Russo+One&family=Open+Sans:wght@800&family=Montserrat:wght@500;700&display=swap" rel="stylesheet">
<style>
  :root {
    --brand-blue: #2190d0;
    --band-blue: #4aa0d6;
    --brand-red: #e0202e;
    --ink: #151515;
    --page: #8a8a8a;
    --white: #ffffff;
    --cash-green: #6cc04a;
  }
  * { margin: 0; padding: 0; box-sizing: border-box; }
  html, body { width: 1200px; height: 1200px; overflow: hidden; }
  body {
    background: var(--page);
    display: flex;
    flex-direction: column;
    align-items: center;
    justify-content: center;
    gap: 44px;
    font-family: "Montserrat", sans-serif;
  }
  .card {
    position: relative;
    width: 900px;
    height: 520px;
    border-radius: 18px;
    overflow: hidden;
  }

  /* Front */
  .card-front { background: var(--white); }
  .photo-backdrop {
    position: absolute; inset: 0;
    background:
      radial-gradient(ellipse at 82% 45%, rgba(238,200,175,0.75), transparent 55%),
      radial-gradient(ellipse at 22% 40%, rgba(205,215,228,0.8), transparent 55%),
      linear-gradient(180deg, #f3f5f8 0%, #e6ebf1 60%, #dfe5ec 100%);
  }
  .wordmark {
    position: absolute; left: 0; right: 0; top: 60px;
    text-align: center;
    font-family: "Russo One", sans-serif;
    color: var(--brand-red);
    line-height: 1;
  }
  .wordmark .name { display: block; font-size: 112px; letter-spacing: 2px; }
  .wordmark .trade { display: block; font-size: 30px; letter-spacing: 11px; margin-top: 22px; }
  .help-band {
    position: absolute; left: 0; right: 0; top: 296px; height: 46px;
    background: var(--band-blue);
    display: flex; align-items: center; justify-content: center; gap: 12px;
    color: var(--white);
    font-family: "Russo One", sans-serif;
    font-size: 24px; letter-spacing: 3px;
  }
  .phone {
    position: absolute; left: 52px; top: 368px;
    display: flex; align-items: center; gap: 12px;
    font-family: "Open Sans", sans-serif; font-weight: 800;
    font-size: 64px; color: var(--ink); letter-spacing: -1px;
  }
  .tagline-band {
    position: absolute; left: 0; right: 0; bottom: 0; height: 62px;
    background: var(--brand-red);
  }
  .tagline {
    position: absolute; left: 54px; bottom: 18px;
    color: var(--white);
    font-family: "Russo One", sans-serif;
    font-size: 22px; letter-spacing: 3px;
  }
  .payment {
    position: absolute; right: 42px; top: 398px;
    width: 290px;
  }
  .payment-label {
    font-weight: 500; font-size: 17px; letter-spacing: 2px;
    color: var(--ink); text-align: center; margin-bottom: 14px;
  }
  .payment-badges { display: flex; justify-content: space-between; }
  .badge {
    width: 86px; height: 54px; border-radius: 5px;
    background: var(--white);
    box-shadow: 0 1px 3px rgba(0,0,0,0.25);
    display: flex; align-items: center; justify-content: center;
  }
  .badge-card-name {
    font-family: "Montserrat", sans-serif; font-weight: 700;
    font-size: 24px; color: #1d3f8f;
  }

  /* Back */
  .card-back {
    background: var(--brand-blue);
    display: flex; align-items: center; justify-content: center;
  }
  .card-back .wordmark { position: static; color: var(--white); }
</style>
</head>
<body>

<section class="card card-front">
  <div class="photo-backdrop" role="img" aria-label="Soft faded photo of hands tightening a chrome sink drain pipe with a red wrench"></div>

  <div class="wordmark">
    <span class="name">RIDGEWAY</span>
    <span class="trade">PLUMBING &amp; DRAINAGE</span>
  </div>

  <div class="help-band">
    <svg width="32" height="24" viewBox="0 0 32 24" aria-hidden="true">
      <rect x="2" y="6" width="18" height="7" rx="2" fill="#fff"/>
      <rect x="9" y="1" width="4" height="6" fill="#fff"/>
      <rect x="5" y="0" width="12" height="3" rx="1.5" fill="#fff"/>
      <path d="M18 6 h6 a4 4 0 0 1 4 4 v4 h-5 v-3 h-5z" fill="#fff"/>
      <circle cx="25.5" cy="19" r="2.2" fill="#fff"/>
    </svg>
    <span>CALL US FOR HELP!</span>
  </div>

  <div class="phone">
    <svg width="36" height="52" viewBox="0 0 36 52" aria-hidden="true">
      <path d="M10 2 l8 10 -5 5 c2 8 6 14 12 19 l5 -5 9 9 -6 8 C14 46 3 28 4 8z" fill="#151515"/>
    </svg>
    <span>0472 318 506</span>
  </div>

  <div class="tagline-band"></div>
  <p class="tagline">YOUR LOCAL PLUMBING EXPERTS</p>

  <div class="payment">
    <p class="payment-label">PAYMENT METHOD</p>
    <div class="payment-badges">
      <div class="badge"><span class="badge-card-name">KOVO</span></div>
      <div class="badge">
        <svg width="60" height="32" viewBox="0 0 60 32" aria-label="Cash" role="img">
          <rect x="4" y="6" width="52" height="22" rx="2" fill="#4e9a35"/>
          <rect x="2" y="3" width="52" height="22" rx="2" fill="var(--cash-green)"/>
          <circle cx="28" cy="14" r="6" fill="#4e9a35"/>
          <circle cx="10" cy="14" r="2" fill="#4e9a35"/>
          <circle cx="46" cy="14" r="2" fill="#4e9a35"/>
        </svg>
      </div>
      <div class="badge">
        <svg width="64" height="34" viewBox="0 0 64 34" aria-label="Cheque" role="img">
          <rect x="1" y="1" width="62" height="32" fill="#f4f6f4" stroke="#b8c2bc"/>
          <rect x="6" y="6" width="12" height="3" fill="#9aa5a0"/>
          <line x1="6" y1="16" x2="58" y2="16" stroke="#b8c2bc"/>
          <line x1="6" y1="22" x2="40" y2="22" stroke="#b8c2bc"/>
          <line x1="42" y1="28" x2="58" y2="28" stroke="#7fa7c6"/>
        </svg>
      </div>
    </div>
  </div>
</section>

<section class="card card-back">
  <div class="wordmark">
    <span class="name">RIDGEWAY</span>
    <span class="trade">PLUMBING &amp; DRAINAGE</span>
  </div>
</section>

</body>
</html>
```